POOL BUILDING CONTRACTOR

our company has shifter focus over the past 18 month we no longer have a retail store and no longer clean pools we build concrete pools. our website if 5 years old we need a completely new site that shows our core product, building concrete pools & renovate concrete pools

here is a few of our competitors;
brantelwaters.com
okvimbuilders.com
ridgeviewlagoonworks.com
plunvora.com
halvertonbasinsandtubs.com
dremblewaterne.com

one we land on a final design I will upload customer before and after photos and any other content needed

Target Market(s)

People looking to build or renovate there pool

Industry/Entity Type

swimming pool

Coding

Coded - Design and coding required

Number of Pages Required

5+ page

Colors
0054AA
0677BA
7BADD7
CADEEF
E8F1F8

Requirements
Must have
• financing Service-Repairs & liners new build-photos renovate-remodeling design-consult customer-reviews Gallery Before-After Contact us 3D Design & Modeling construction process & Timeline Equipment Features Hardscapes I like these sites https://meadowlarkbasinsbycraft.com/ https://holtbergwaters.com/

```html
<!DOCTYPE html>
<html lang="en">
<head>
<meta charset="utf-8">
<title>Aquaverne — Premium Pool Builders</title>
<link rel="stylesheet" href="https://fonts.googleapis.com/css2?family=Inter:wght@400;500;600;700&display=swap">
<style>
:root{
  --slate:#3e5878;
  --slate-dark:#30475f;
  --ink:#111;
  --sky:#2bbdf0;
  --sky-pale:#d7f2fc;
  --white:#fff;
  --star:#3a5bd9;
}
*{box-sizing:border-box;margin:0;padding:0}
html,body{width:1200px;height:4117px;overflow:hidden}
body{font-family:"Inter",sans-serif;color:var(--ink);background:var(--white);position:relative}
.abs{position:absolute}
.photo{position:absolute}

/* top bar + nav */
.topbar{left:0;top:0;width:1200px;height:32px;background:var(--slate);color:#fff;font-size:12px;font-weight:600;display:flex;align-items:center;justify-content:center;gap:6px}
.nav{left:0;top:32px;width:1200px;height:96px;background:#fff}
.nav a{position:absolute;top:38px;font-size:16px;font-weight:600;color:var(--ink);text-decoration:none}
.nav .active{border-bottom:3px solid var(--slate);padding-bottom:12px;padding-left:8px;padding-right:8px;margin-left:-8px}
.brand{display:flex;align-items:center;gap:8px;font-weight:700;color:var(--slate)}
.brand .mark{border-radius:50%;background:var(--sky)}

/* hero */
.hero{left:0;top:128px;width:1200px;height:550px;background:linear-gradient(180deg,#6aa7c4 0%,#3d87b0 45%,#2b78a8 100%)}
.hero h1{position:absolute;left:0;width:1170px;top:180px;text-align:center;font-size:54px;font-weight:700;color:#fff;letter-spacing:.5px}
.hero p{position:absolute;left:0;width:1260px;top:272px;text-align:center;font-size:20px;font-weight:600;color:#fff;line-height:29px}
.btn-hero{position:absolute;left:556px;top:356px;width:146px;height:36px;background:var(--slate);color:#fff;font-size:12px;font-weight:600;border-radius:4px;display:flex;align-items:center;justify-content:center}

/* about */
.video{left:85px;top:765px;width:535px;height:326px;border-radius:8px;background:linear-gradient(180deg,#5e9fd6 0%,#a9d4ea 42%,#2aa2c9 62%,#1678a6 100%)}
.play{position:absolute;left:232px;top:128px;width:70px;height:70px;border-radius:50%;background:rgba(255,255,255,.9)}
.play::after{content:"";position:absolute;left:28px;top:22px;border-left:20px solid var(--slate);border-top:13px solid transparent;border-bottom:13px solid transparent}
.about-rule{left:677px;top:784px;width:4px;height:96px;background:var(--slate)}
.eyebrow{font-size:12px;font-weight:600;text-transform:uppercase}
.about-title{left:697px;top:812px;font-size:30px;font-weight:700;line-height:38px;width:420px}
.about-copy{left:675px;top:900px;width:412px;font-size:13px;line-height:20px}
.feature{display:flex;align-items:center;gap:14px;font-size:13px;font-weight:600;line-height:16px}
.ring{width:56px;height:56px;border-radius:50%;background:var(--slate);display:flex;align-items:center;justify-content:center}

/* services */
.services{left:0;top:1224px;width:1200px;height:606px;background:var(--sky-pale)}
.center{text-align:center;width:1200px;left:0}
.section-title{font-size:28px;font-weight:600}
.card{position:absolute;top:1425px;width:242px;height:221px;overflow:hidden}
.card .frame{position:absolute;left:16px;top:16px;right:16px;bottom:16px;border:1px solid var(--sky)}
.card .label{position:absolute;left:0;right:0;top:86px;text-align:center;color:#fff;font-size:16px;font-weight:600;line-height:20px;text-shadow:0 1px 3px rgba(0,0,0,.4)}
.card .more{position:absolute;left:58px;top:140px;width:126px;height:30px;background:var(--slate);color:#fff;font-size:11px;font-weight:600;border-radius:15px;display:flex;align-items:center;justify-content:center}

.consult{left:91px;top:1740px;width:1016px;height:163px;background:var(--slate);color:#fff}
.consult h3{position:absolute;left:49px;top:48px;font-size:27px;font-weight:500}
.consult p{position:absolute;left:52px;top:93px;font-size:16px}
.btn-sky{position:absolute;background:var(--sky);color:#fff;font-size:11px;font-weight:600;border-radius:4px;display:flex;align-items:center;justify-content:center}

/* process */
.step{position:absolute;top:2067px;width:260px;text-align:center}
.step .icon{width:90px;height:90px;margin:0 auto;border-radius:50%;border:4px solid var(--sky);background:var(--slate);display:flex;align-items:center;justify-content:center;position:relative}
.step .num{position:absolute;left:-12px;top:4px;width:20px;height:20px;border-radius:50%;background:var(--sky);font-size:11px;color:#111;display:flex;align-items:center;justify-content:center}
.step h4{font-size:20px;font-weight:500;margin-top:16px}
.step p{font-size:13px;line-height:20px;margin:12px auto 0;width:200px}
.dots-line{position:absolute;top:2111px;height:0;border-top:1px dashed #444}

/* gallery */
.arrow{position:absolute;top:2602px;width:48px;height:48px;display:flex;align-items:center;justify-content:center}
.pager span{display:inline-block;width:9px;height:9px;border-radius:50%;background:#ccc;margin:0 3px}
.pager span.on{background:#111}

/* testimonials */
.testi-bg{left:0;top:2868px;width:1200px;height:504px;background:linear-gradient(180deg,#b9dbe8 0%,#8ec6dc 50%,#5fb1d4 100%)}
.review{position:absolute;top:3014px;width:307px;height:232px;background:#fff;padding:20px 22px}
.review .head{display:flex;justify-content:space-between;align-items:center}
.stars{color:var(--star);font-size:16px;letter-spacing:1px}
.tag{font-size:9px;font-weight:700;display:flex;align-items:center;gap:4px}
.tag i{width:10px;height:10px;border-radius:50%;background:var(--star);display:inline-block}
.review p{font-size:12.5px;line-height:18px}
.who{position:absolute;left:22px;bottom:24px;display:flex;align-items:center;gap:6px}
.who .av{width:26px;height:26px;border-radius:50%;background:#b8c3d6}
.who b{font-size:11px;display:block}
.who small{font-size:8px;color:#777}

/* cta */
.cta{left:0;top:3372px;width:1200px;height:160px;background:var(--sky)}
.cta h3{position:absolute;left:236px;top:56px;color:#fff;font-size:26px;font-weight:600;line-height:38px}
.btn-slate{position:absolute;background:var(--slate);color:#fff;font-size:11px;font-weight:600;border-radius:5px;display:flex;align-items:center;justify-content:center}

/* footer */
.footer{left:0;top:3532px;width:1200px;height:511px;background:var(--slate);color:#fff}
.pill{left:96px;top:3509px;width:307px;height:111px;background:#fff;border:4px solid var(--slate);border-radius:56px;display:flex;align-items:center;justify-content:center}
.contact{position:absolute;left:106px;display:flex;align-items:center;gap:12px;font-size:13px;color:#fff}
.field{position:absolute;background:#fff;color:#555;font-size:12.5px;padding-left:18px;display:flex;align-items:center}
.social{position:absolute;top:3895px;width:18px;height:18px;border-radius:50%;background:#fff}
.bottombar{left:0;top:4043px;width:1200px;height:74px;background:var(--slate-dark);color:#fff}
.bottombar a{position:absolute;top:27px;font-size:16px;font-weight:500;color:#fff;text-decoration:none}
</style>
</head>
<body>

<div class="abs topbar">SCHEDULE YOUR CONSULTATION TODAY
  <svg width="13" height="13" viewBox="0 0 24 24" fill="none" stroke="#fff" stroke-width="2"><path d="M5 3h4l2 5-3 2a12 12 0 0 0 6 6l2-3 5 2v4a2 2 0 0 1-2 2A18 18 0 0 1 3 5a2 2 0 0 1 2-2z"/></svg>
  812-555-0147</div>

<nav class="abs nav">
  <a class="active" style="left:92px">HOME</a>
  <a style="left:175px">ABOUT US</a>
  <a style="left:283px">OUR SERVICES <svg width="12" height="8" viewBox="0 0 12 8"><path d="M1 1l5 5 5-5" fill="none" stroke="#444" stroke-width="1.5"/></svg></a>
  <div class="brand" style="position:absolute;left:470px;top:20px;font-size:40px"><span class="mark" style="width:52px;height:52px"></span>Aquaverne</div>
  <a style="left:786px">GALLERY</a>
  <a style="left:879px">TESTIMONIALS</a>
  <a style="left:1025px">CONTACT</a>
</nav>

<section class="abs hero" role="img" aria-label="Resort swimming pool with palm trees, loungers and a pergola under a blue sky">
  <h1>PREMIUM POOL BUILDERS</h1>
  <p>Contact us today to begin the process of<br>your dream swimming pool.</p>
  <div class="btn-hero">GET STARTED</div>
</section>

<div class="photo video" role="img" aria-label="Video still of an infinity pool beside a palm-lined beach"><div class="play"></div></div>
<div class="abs about-rule"></div>
<div class="abs eyebrow" style="left:697px;top:784px">About</div>
<h2 class="abs about-title">Aquaverne The Pool Service Company</h2>
<p class="abs about-copy">Lorem ipsum dolor sit amet consectetur. In purus tempus malesuada tortor eget. Tincidunt facilisi adipiscing id vestibulum nunc mattis velit. Lacus mauris vitae orci in interdum adipiscing egestas diam. Cum integer in nunc et. .</p>
<div class="abs feature" style="left:675px;top:1013px"><span class="ring"><svg width="28" height="28" viewBox="0 0 24 24" fill="none" stroke="#fff" stroke-width="1.8"><path d="M8 3v14M16 3v14M8 7h8M8 12h8M2 19c2 2 4 2 5 0 1 2 4 2 5 0 1 2 4 2 5 0 1 2 3 2 5 0"/></svg></span>TRUSTED POOL<br>CONSTRUCTIONS</div>
<div class="abs feature" style="left:878px;top:1013px"><span class="ring"><svg width="30" height="30" viewBox="0 0 24 24" fill="none" stroke="#fff" stroke-width="1.8"><circle cx="12" cy="12" r="9"/><path d="M8 12l3 3 5-6"/></svg></span>QUALITY &amp;<br>EXPERT</div>

<section class="abs services"></section>
<div class="abs center eyebrow" style="top:1295px">Our Services</div>
<h2 class="abs center section-title" style="top:1328px">Experienced Swimming Pool Builder Company</h2>

<div class="card" style="left:91px;background:linear-gradient(180deg,#b9d6e4,#3aa0bd)" role="img" aria-label="Newly built pool with a city skyline behind"><div class="frame"></div><div class="label">Pool Construction</div><div class="more">LEARN MORE</div></div>
<div class="card" style="left:358px;background:linear-gradient(180deg,#5e8f6a,#2a6fa3 60%,#a8633e)" role="img" aria-label="Remodeled pool with wooden deck and tropical garden"><div class="frame"></div><div class="label">Renovations &amp;<br>Remodeling</div><div class="more">LEARN MORE</div></div>
<div class="card" style="left:625px;background:linear-gradient(135deg,#c79b83,#9fc4cf 55%,#7cb4c7)" role="img" aria-label="Pool liner and safety cover over water"><div class="frame"></div><div class="label">Liners &amp; Covers</div><div class="more">LEARN MORE</div></div>
<div class="card" style="left:890px;background:linear-gradient(135deg,#d8d4cd,#9ba6b3)" role="img" aria-label="Calculator and paperwork for pool financing"><div class="frame"></div><div class="label">Financing</div><div class="more">LEARN MORE</div></div>

<section class="abs consult">
  <h3>Need a consultation?</h3>
  <p>We are happy to discuss your project with you. Schedule a free consultation now!</p>
  <div class="btn-sky" style="left:768px;top:79px;width:178px;height:37px">Request a Call Back</div>
</section>

<div class="abs center eyebrow" style="top:1973px">Our Process</div>
<h2 class="abs center section-title" style="top:1998px">Building Your Dream Pool</h2>
<div class="dots-line" style="left:376px;width:175px"></div>
<div class="dots-line" style="left:684px;width:175px"></div>
<div class="step" style="left:187px"><div class="icon"><span class="num">1</span><svg width="40" height="40" viewBox="0 0 24 24" fill="none" stroke="#fff" stroke-width="1.6"><path d="M9 18h6M10 21h4M12 3a6 6 0 0 0-3 11v2h6v-2a6 6 0 0 0-3-11z"/></svg></div><h4>Design</h4><p>Lorem ipsum dolor sit amet consectetur. Cursus accumsan donec faucibus lobortis ut. Diam nunc id in amet nunc phasellus.</p></div>
<div class="step" style="left:484px"><div class="icon"><span class="num">2</span><svg width="40" height="40" viewBox="0 0 24 24" fill="none" stroke="#fff" stroke-width="1.6"><path d="M2 8h3l3 8h9l3-7H7"/><circle cx="9" cy="19" r="1.6"/><circle cx="16" cy="19" r="1.6"/></svg></div><h4>Construction</h4><p>Lorem ipsum dolor sit amet consectetur. Cursus accumsan donec faucibus lobortis ut. Diam nunc id in amet nunc phasellus.</p></div>
<div class="step" style="left:800px"><div class="icon"><span class="num">3</span><svg width="40" height="40" viewBox="0 0 24 24" fill="none" stroke="#fff" stroke-width="1.6"><rect x="4" y="6" width="16" height="14" rx="1"/><path d="M9 6V3h6v3M7 16c2-2 3 2 5 0s3 2 5 0"/></svg></div><h4>Handover</h4><p>Lorem ipsum dolor sit amet consectetur. Cursus accumsan donec faucibus lobortis ut. Diam nunc id in amet nunc phasellus.</p></div>

<div class="abs center eyebrow" style="top:2397px;left:-10px">View our range of</div>
<h2 class="abs center section-title" style="top:2415px;left:-10px">Gallery Projects</h2>
<div class="photo" style="left:0;top:2499px;width:306px;height:253px;background:linear-gradient(180deg,#5e7a55 0%,#7c9a6c 45%,#2f93c9 60%,#1677b6 100%)" role="img" aria-label="Hillside infinity pool beside a pavilion"></div>
<div class="photo" style="left:346px;top:2474px;width:604px;height:304px;background:linear-gradient(180deg,#d9dfe2 0%,#8fa38a 38%,#4fb2d2 62%,#2a8fb8 100%)" role="img" aria-label="Poolside loungers under white umbrellas with a water jet"></div>
<div class="photo" style="left:990px;top:2499px;width:210px;height:253px;background:linear-gradient(180deg,#4f8fd0 0%,#a7cbe2 40%,#2aa4cf 65%,#127cb0 100%)" role="img" aria-label="Pool framed by palm trees"></div>
<div class="arrow" style="left:322px;background:#5c6470"><svg width="14" height="22" viewBox="0 0 14 22"><path d="M11 2L3 11l8 9" fill="none" stroke="#fff" stroke-width="1.8"/></svg></div>
<div class="arrow" style="left:926px;background:var(--sky)"><svg width="14" height="22" viewBox="0 0 14 22"><path d="M3 2l8 9-8 9" fill="none" stroke="#fff" stroke-width="1.8"/></svg></div>
<div class="abs center pager" style="top:2830px;left:43px"><span class="on"></span><span></span><span></span></div>

<section class="abs testi-bg" role="img" aria-label="Faded poolside scene with palms and loungers"></section>
<div class="abs center eyebrow" style="top:2920px">Testimonials</div>
<h2 class="abs center section-title" style="top:2944px">What Our Clients Say</h2>
<div class="review" style="left:105px"><div class="head"><span class="stars">★★★★★</span><span class="tag"><i></i>Testimonial</span></div><p style="margin-top:28px">Dude, your stuff is the bomb! House rent is the real deal! I STRONGLY recommend house rent to EVERYONE interested in running a successful online business!</p><div class="who"><span class="av"></span><span><b>Dara Holloway</b><small>Senior Planning Strategist</small></span></div></div>
<div class="review" style="left:435px"><div class="head"><span class="stars">★★★★★</span><span class="tag"><i></i>Testimonial</span></div><p style="margin-top:14px;line-height:15.5px">"I like Aquaverne more and more each day because it makes my life a lot easier. We can't understand how we've been living without Aquaverne. Aquaverne has got everything I need. The service was excellent."</p><div class="who"><span class="av"></span><span><b>Mrs. Elsbeth Korr</b><small>Legacy Usability Manager</small></span></div></div>
<div class="review" style="left:764px"><div class="head"><span class="stars">★★★★★</span><span class="tag"><i></i>Testimonial</span></div><p style="margin-top:38px">You've saved our business! Aquaverne has got everything I need. We were treated like royalty. It's really wonderful.</p><div class="who"><span class="av"></span><span><b>Tobin Marsh</b><small>District Assurance Officer</small></span></div></div>

<section class="abs cta">
  <h3>Ready to build your pool?<br>It Starts Here.</h3>
  <div class="btn-slate" style="left:794px;top:64px;width:178px;height:37px">Request a Call Back</div>
</section>

<footer class="abs footer"></footer>
<div class="abs pill"><div class="brand" style="font-size:34px"><span class="mark" style="width:40px;height:40px"></span>Aquaverne</div></div>
<h3 class="abs" style="left:624px;top:3620px;color:#fff;font-size:25px;font-weight:500">BUILD YOUR DREAM POOL TODAY</h3>
<div class="contact" style="top:3675px"><svg width="24" height="24" viewBox="0 0 24 24" fill="none" stroke="#fff" stroke-width="2"><path d="M5 3h4l2 5-3 2a12 12 0 0 0 6 6l2-3 5 2v4a2 2 0 0 1-2 2A18 18 0 0 1 3 5a2 2 0 0 1 2-2z"/></svg>(754) 555-0192</div>
<div class="contact" style="top:3722px"><svg width="26" height="20" viewBox="0 0 26 20" fill="none" stroke="#fff" stroke-width="2"><rect x="1" y="2" width="24" height="16"/><path d="M1 2l12 9 12-9"/></svg>hello@aquaverne.example</div>
<div class="contact" style="top:3768px"><svg width="24" height="28" viewBox="0 0 24 28" fill="none" stroke="#fff" stroke-width="2"><path d="M12 26s9-9 9-15a9 9 0 0 0-18 0c0 6 9 15 9 15z"/><circle cx="12" cy="11" r="3"/></svg>Your Location here</div>
<div class="abs" style="left:92px;top:3862px;color:#fff;font-size:12.5px;font-weight:500">CONNECTED WITH US</div>
<span class="social" style="left:95px"></span><span class="social" style="left:130px"></span><span class="social" style="left:165px"></span><span class="social" style="left:200px"></span><span class="social" style="left:234px"></span>

<div class="field" style="left:623px;top:3700px;width:232px;height:38px">First name</div>
<div class="field" style="left:876px;top:3700px;width:232px;height:38px">Last name</div>
<div class="field" style="left:623px;top:3759px;width:232px;height:38px">Email</div>
<div class="field" style="left:876px;top:3759px;width:232px;height:38px">Phone Number</div>
<div class="field" style="left:623px;top:3826px;width:482px;height:126px;align-items:flex-start;padding-top:20px;padding-left:27px">Your message</div>
<div class="btn-sky" style="left:623px;top:3971px;width:126px;height:37px;border-radius:3px">SEND</div>

<div class="abs bottombar">
  <a style="left:90px">HOME</a><a style="left:162px">ABOUT US</a><a style="left:270px">OUR SERVICES</a><a style="left:418px">GALLERY</a><a style="left:511px">TESTIMONIALS</a><a style="left:656px">CONTACT</a>
  <span style="position:absolute;left:876px;top:29px;font-size:12.5px">©2023 AQUAVERNE . All rights reserved.</span>
</div>

</body>
</html>
```